Moving Postcard

I need a postcard to let people know my law firm is moving effective Jan 1 2018 to Harlow Tower Suite 2700 2836 Larkmoor Street Seattle Washington 98127-3460. A copy of my current letterhead, business card, and envelope (all of which I like) are attached. The color is odd on the scan but it's a dark purple or purplish-brown. I was to keep the 'careful, confident defense' (but drop the criminal) and perhaps specify elsewhere I'm talking about criminal defense, lawyer discipline defense, and judicial conduct defense. I'd like a design I can easily upload and have printed by Zint

Law Firm

```html
<!DOCTYPE html>
<html lang="en">
<head>
<meta charset="utf-8">
<title>Rowan Ellery – New Address Postcard</title>
<link rel="stylesheet" href="https://fonts.googleapis.com/css2?family=Noto+Serif:ital,wght@1,600&family=Carlito:ital,wght@0,400;0,700;1,400;1,700&display=swap">
<style>
  :root {
    --plum: #4a3036;
    --plum-line: #7a5a60;
    --card-grey: #e2e1e1;
    --skyline-grey: #dcdbdb;
    --banner: #e6dcdc;
    --ink: #4a3f41;
    --name-muted: #a39394;
    --text-light: #f3eeee;
    --page: #ffffff;
  }
  * { margin: 0; padding: 0; box-sizing: border-box; }
  html, body { width: 801px; height: 1200px; overflow: hidden; background: var(--page); }
  body { position: relative; font-family: "Carlito", "Calibri", sans-serif; }

  .card {
    position: absolute;
    left: 33px;
    width: 704px;
    height: 545px;
    overflow: hidden;
    box-shadow: 8px 10px 14px rgba(0,0,0,0.35);
  }
  .card--front { top: 30px; background: var(--plum); }
  .card--back { top: 589px; background: var(--card-grey); border: 1px solid #cfcfcf; }

  .firm-name {
    position: absolute;
    font-family: "Carlito", "Calibri", sans-serif;
    font-weight: 700;
    font-size: 48px;
    line-height: 1;
    letter-spacing: 0.5px;
  }
  .tagline {
    position: absolute;
    font-family: "Noto Serif", serif;
    font-style: italic;
    font-weight: 600;
    font-size: 18px;
    line-height: 1;
  }
  address { font-style: normal; }

  /* Front */
  .card--front .firm-name { left: 40px; width: 350px; top: 78px; text-align: center; color: var(--text-light); }
  .card--front .tagline { left: 40px; width: 350px; top: 128px; text-align: center; color: var(--text-light); }
  .contact-front { position: absolute; left: 446px; top: 106px; color: var(--text-light); }
  .contact-front .phone { font-weight: 700; font-size: 18px; line-height: 23px; }
  .contact-front .web { font-size: 15.5px; line-height: 20px; }
  .address-front {
    position: absolute; left: 446px; top: 192px;
    color: var(--text-light); font-weight: 700; font-size: 18px; line-height: 23.5px;
  }

  .banner { position: absolute; left: 0; top: 210px; width: 396px; height: 60px; }
  .banner svg { position: absolute; inset: 0; }
  .banner-title {
    position: absolute; left: 0; width: 372px; top: 9px; text-align: center;
    font-weight: 700; font-style: italic; font-size: 21px; line-height: 24px; color: var(--ink); letter-spacing: 0.3px;
  }
  .banner-date {
    position: absolute; left: 0; width: 372px; top: 35px; text-align: center;
    font-style: italic; font-size: 13.5px; line-height: 16px; color: var(--ink);
  }

  .skyline {
    position: absolute; left: 0; right: 0; top: 330px; bottom: 0;
    background: linear-gradient(to bottom, var(--plum) 0%, #8e7d80 45%, var(--skyline-grey) 72%, var(--skyline-grey) 100%);
  }

  /* Back */
  .card--back .firm-name { left: 29px; top: 62px; color: var(--name-muted); }
  .card--back .tagline { left: 69px; top: 120px; font-size: 16px; color: var(--ink); }
  .services {
    position: absolute; left: 60px; top: 168px; list-style: none;
    color: var(--ink); font-size: 15px; line-height: 30px; letter-spacing: 0.2px;
  }
  .divider { position: absolute; left: 62px; top: 250px; width: 229px; border-top: 1.5px solid #6a5c5e; }
  .address-back {
    position: absolute; left: 60px; width: 230px; top: 290px; text-align: center;
    color: var(--ink); font-weight: 700; font-size: 16.5px; line-height: 22px;
  }
  .contact-back { position: absolute; left: 40px; width: 270px; top: 398px; text-align: center; color: var(--ink); }
  .contact-back .phone { font-weight: 700; font-size: 18px; line-height: 22px; }
  .contact-back .web { font-size: 14.5px; line-height: 19px; }

  .stamp-box {
    position: absolute; left: 550px; top: 48px; width: 112px; height: 109px;
    border: 1.5px dashed var(--plum-line);
  }
  .mail-line { position: absolute; left: 370px; width: 288px; border-top: 1.5px dashed var(--plum-line); }
  .mail-line--1 { top: 296px; }
  .mail-line--2 { top: 359px; }
  .mail-line--3 { top: 424px; }
</style>
</head>
<body>

<section class="card card--front">
  <h1 class="firm-name">ROWAN ELLERY</h1>
  <p class="tagline">careful, confident defense</p>

  <div class="contact-front">
    <p class="phone">(206) 555-0147</p>
    <p class="web">ellerydefenselaw.com</p>
  </div>

  <address class="address-front">
    Harlow Tower Suite 2700<br>
    2836 Larkmoor Street<br>
    Seattle, Washington<br>
    98127-3460
  </address>

  <div class="banner">
    <svg width="396" height="60" viewBox="0 0 396 60" aria-hidden="true">
      <polygon points="0,0 374,0 396,30 374,60 0,60" fill="var(--banner)"/>
    </svg>
    <p class="banner-title">WE HAVE A NEW ADDRESS</p>
    <p class="banner-date">Effective January 1, 2018</p>
  </div>

  <div class="skyline" role="img" aria-label="Silhouette of a city skyline with an observation tower"></div>
</section>

<section class="card card--back">
  <h2 class="firm-name">ROWAN ELLERY</h2>
  <p class="tagline">careful, confident defense</p>

  <ul class="services">
    <li>LAWYER MISCONDUCT DEFENSE</li>
    <li>JUDICIAL MISCONDUCT DEFENSE</li>
  </ul>

  <div class="divider"></div>

  <address class="address-back">
    Harlow Tower Suite 2700<br>
    2836 Larkmoor Street<br>
    Seattle, Washington<br>
    98127-3460
  </address>

  <div class="contact-back">
    <p class="phone">(206) 555-0147</p>
    <p class="web">ellerydefenselaw.com</p>
  </div>

  <div class="stamp-box"></div>
  <div class="mail-line mail-line--1"></div>
  <div class="mail-line mail-line--2"></div>
  <div class="mail-line mail-line--3"></div>
</section>

</body>
</html>
```